Banner Ad to promote Youth Cycling Camps

We need a 728 x 90 banner ad to promote some youth cycling camps. There are 2 different camps - a road camp where they learn to ride their bikes on the roads and a mountain bike camp. The camps teach bike handling skills and racing tactics.

Target Market(s)

Parents of youth ages 7-17

Industry/Entity Type

Non-Profit

Font styles to use
Sans Serif

Requirements
Must have
• Logo
• Dates - Road Camp May 5-7, 2017
• - Mountain Bike Camp July 14-16, 2017
• website - quadrapedalcup.org
• be 728 x 90
Nice to have
• Animated - would like it to rotate with 3 slides - 1 a focus on both camps, 1 on road camp, 1 on mountain bike camp

```html
<!DOCTYPE html>
<html lang="en">
<head>
<meta charset="utf-8">
<title>Youth Cycling Camps – Banner Frames</title>
<link rel="stylesheet" href="https://fonts.googleapis.com/css2?family=Arimo:ital,wght@0,400;0,700;1,700&display=swap">
<style>
  :root {
    --page: #ffffff;
    --label: #333333;
    --frame-border: #8a8a8a;
    --brand-pink: #e0157e;
    --brand-pink-light: #f05aa6;
    --brand-blue: #5cc3ef;
    --brand-yellow: #f0e935;
    --headline: #ffffff;
    --subline: #f7ec2b;
    --logo-ink: #1b1b1b;
    --web-ink: #4a4a4a;
    --button-navy: #1c1f5a;
  }
  html, body {
    margin: 0;
    width: 1200px;
    height: 1200px;
    overflow: hidden;
    background: var(--page);
    font-family: "Arimo", Arial, sans-serif;
  }
  .board { position: relative; width: 1200px; height: 1200px; }

  .frame-label {
    position: absolute;
    left: 20px;
    font-size: 24px;
    color: var(--label);
    letter-spacing: 0.5px;
  }
  .frame-a-label { top: 344px; }
  .frame-b-label { top: 498px; }
  .frame-c-label { top: 652px; }

  .banner-slot {
    position: absolute;
    left: 155px;
    width: 1028px;
    height: 127px;
  }
  .slot-a { top: 298px; }
  .slot-b { top: 452px; }
  .slot-c { top: 606px; }

  .banner {
    position: absolute;
    left: 0; top: 0;
    width: 728px;
    height: 90px;
    transform: scale(1.4121);
    transform-origin: 0 0;
    background: #fff;
    outline: 1px solid var(--frame-border);
    overflow: hidden;
  }
  .banner-shapes { position: absolute; left: 0; top: 0; width: 728px; height: 90px; }

  .brand {
    position: absolute;
    left: 14px; top: 18px;
    width: 150px;
    display: flex;
    align-items: center;
    gap: 7px;
  }
  .brand-dot {
    width: 16px; height: 16px;
    border-radius: 50%;
    background: var(--brand-blue);
    flex: none;
  }
  .brand-name {
    font-size: 17px;
    font-weight: 700;
    line-height: 1.05;
    color: var(--logo-ink);
  }
  .website {
    position: absolute;
    left: 37px; top: 58px;
    margin: 0;
    font-size: 11px;
    font-weight: 400;
    color: var(--web-ink);
  }

  .headline {
    position: absolute;
    left: 290px; top: 4px;
    width: 240px;
    margin: 0;
    text-align: center;
    font-size: 17px;
    font-weight: 700;
    line-height: 19px;
    color: var(--headline);
    text-shadow: 1px 1px 1px rgba(0,0,0,0.6);
  }
  .subline {
    position: absolute;
    left: 272px; top: 42px;
    width: 290px;
    margin: 0;
    text-align: center;
    font-size: 12.3px;
    font-weight: 700;
    font-style: italic;
    line-height: 14px;
    color: var(--subline);
    text-shadow: 1px 1px 1px rgba(0,0,0,0.5);
  }

  .photo {
    position: absolute;
    left: 555px; top: 0;
    width: 173px; height: 76px;
    clip-path: polygon(0 0, 100% 0, 100% 100%, 37.5% 100%);
  }
  .photo-group { background: linear-gradient(120deg, #6d7fa8 0%, #2d3c6e 40%, #a33a3a 70%, #3b4a78 100%); }
  .photo-trail { background: linear-gradient(120deg, #4e6a3a 0%, #27361f 45%, #7a8f5a 75%, #3f4f2e 100%); }
  .photo-road { background: linear-gradient(120deg, #c9cbcf 0%, #8d9096 45%, #2a2d35 70%, #b8bac0 100%); }

  .cta {
    position: absolute;
    left: 566px; top: 45px;
    width: 152px; height: 36px;
    border-radius: 9px;
    background: linear-gradient(to bottom, var(--brand-pink-light) 0%, var(--brand-pink) 55%, #c10c68 100%);
    box-shadow: 0 1px 2px rgba(0,0,0,0.45);
    color: #fff;
    text-decoration: none;
    font-size: 17px;
    line-height: 36px;
    padding-left: 11px;
    box-sizing: border-box;
  }
  .cta-divider {
    position: absolute;
    right: 34px; top: 2px;
    width: 1px; height: 32px;
    background: rgba(255,255,255,0.55);
  }
  .cta-icon {
    position: absolute;
    right: 6px; top: 7px;
    width: 22px; height: 22px;
  }

  .caption {
    position: absolute;
    left: 0; top: 790px;
    width: 1302px;
    text-align: center;
    font-size: 48px;
    color: var(--label);
    margin: 0;
    font-weight: 400;
  }
</style>
</head>
<body>
<main class="board">

  <span class="frame-label frame-a-label">FRAME A</span>
  <span class="frame-label frame-b-label">FRAME B</span>
  <span class="frame-label frame-c-label">FRAME C</span>

  <!-- Frame A: both camps -->
  <div class="banner-slot slot-a">
    <section class="banner">
      <svg class="banner-shapes" viewBox="0 0 728 90" aria-hidden="true">
        <defs>
          <linearGradient id="panelFill" x1="0" y1="0" x2="0" y2="1">
            <stop offset="0" stop-color="#555"/><stop offset="1" stop-color="#333"/>
          </linearGradient>
          <linearGradient id="greenStripe" x1="0" y1="0" x2="1" y2="1">
            <stop offset="0" stop-color="#e6f5c8"/><stop offset="1" stop-color="#7dbb2e"/>
          </linearGradient>
        </defs>
        <path d="M170,90 C232,80 276,44 290,0 L304,0 C292,46 268,72 248,90 Z" fill="#e0157e"/>
        <path d="M198,90 C246,78 278,50 294,6 L298,8 C284,50 258,76 232,90 Z" fill="#f7b6d6"/>
        <path d="M300,0 L535,0 L600,76 L250,76 C274,52 292,26 300,0 Z" fill="url(#panelFill)"/>
        <path d="M535,0 L556,0 L622,76 L600,76 Z" fill="url(#greenStripe)"/>
        <rect x="248" y="76" width="297" height="14" fill="#5cc3ef"/>
        <rect x="545" y="76" width="183" height="14" fill="#f0e935"/>
      </svg>
      <div class="brand"><span class="brand-dot"></span><span class="brand-name">Quadrapedal<br>Cup</span></div>
      <p class="website">quadrapedalcup.org</p>
      <h2 class="headline">THE YOUTH CYCLING<br>CAMPS</h2>
      <p class="subline">Learn how to ride the bike on the road<br>and the mountain, skills and tactics</p>
      <div class="photo photo-group" role="img" aria-label="Photo of a large group of young cyclists in helmets posing together"></div>
      <a class="cta" href="#">Learn more<span class="cta-divider"></span>
        <svg class="cta-icon" viewBox="0 0 22 22" aria-hidden="true"><circle cx="11" cy="11" r="10" fill="#fff"/><circle cx="11" cy="11" r="8.3" fill="var(--button-navy)"/><path d="M9,7 L15,11 L9,15 Z" fill="#fff"/></svg>
      </a>
    </section>
  </div>

  <!-- Frame B: mountain bike camp -->
  <div class="banner-slot slot-b">
    <section class="banner">
      <svg class="banner-shapes" viewBox="0 0 728 90" aria-hidden="true">
        <path d="M170,90 C232,80 276,44 290,0 L304,0 C292,46 268,72 248,90 Z" fill="#e0157e"/>
        <path d="M198,90 C246,78 278,50 294,6 L298,8 C284,50 258,76 232,90 Z" fill="#f7b6d6"/>
        <path d="M300,0 L535,0 L600,76 L250,76 C274,52 292,26 300,0 Z" fill="url(#panelFill)"/>
        <path d="M535,0 L556,0 L622,76 L600,76 Z" fill="url(#greenStripe)"/>
        <rect x="248" y="76" width="297" height="14" fill="#5cc3ef"/>
        <rect x="545" y="76" width="183" height="14" fill="#f0e935"/>
      </svg>
      <div class="brand"><span class="brand-dot"></span><span class="brand-name">Quadrapedal<br>Cup</span></div>
      <p class="website">quadrapedalcup.org</p>
      <h2 class="headline">THE YOUTH CYCLING<br>CAMPS</h2>
      <p class="subline">Mountain Bike Camp: July 14-16, 2017<br>Trail handling skills and race tactics</p>
      <div class="photo photo-trail" role="img" aria-label="Photo of young mountain bikers riding on a forest trail"></div>
      <a class="cta" href="#">Learn more<span class="cta-divider"></span>
        <svg class="cta-icon" viewBox="0 0 22 22" aria-hidden="true"><circle cx="11" cy="11" r="10" fill="#fff"/><circle cx="11" cy="11" r="8.3" fill="var(--button-navy)"/><path d="M9,7 L15,11 L9,15 Z" fill="#fff"/></svg>
      </a>
    </section>
  </div>

  <!-- Frame C: road camp -->
  <div class="banner-slot slot-c">
    <section class="banner">
      <svg class="banner-shapes" viewBox="0 0 728 90" aria-hidden="true">
        <path d="M170,90 C232,80 276,44 290,0 L304,0 C292,46 268,72 248,90 Z" fill="#e0157e"/>
        <path d="M198,90 C246,78 278,50 294,6 L298,8 C284,50 258,76 232,90 Z" fill="#f7b6d6"/>
        <path d="M300,0 L535,0 L600,76 L250,76 C274,52 292,26 300,0 Z" fill="url(#panelFill)"/>
        <path d="M535,0 L556,0 L622,76 L600,76 Z" fill="url(#greenStripe)"/>
        <rect x="248" y="76" width="297" height="14" fill="#5cc3ef"/>
        <rect x="545" y="76" width="183" height="14" fill="#f0e935"/>
      </svg>
      <div class="brand"><span class="brand-dot"></span><span class="brand-name">Quadrapedal<br>Cup</span></div>
      <p class="website">quadrapedalcup.org</p>
      <h2 class="headline">THE YOUTH CYCLING<br>CAMPS</h2>
      <p class="subline">Road Camp: May 5-7, 2017<br>Bike handling skills and racing tactics</p>
      <div class="photo photo-road" role="img" aria-label="Photo of young road cyclists riding on pavement"></div>
      <a class="cta" href="#">Learn more<span class="cta-divider"></span>
        <svg class="cta-icon" viewBox="0 0 22 22" aria-hidden="true"><circle cx="11" cy="11" r="10" fill="#fff"/><circle cx="11" cy="11" r="8.3" fill="var(--button-navy)"/><path d="M9,7 L15,11 L9,15 Z" fill="#fff"/></svg>
      </a>
    </section>
  </div>

  <p class="caption">Animated style</p>
</main>
</body>
</html>
```